Boutique Fitness Facility needs a new meal plan design that is as hot as our workouts!

We are about to host our 6 week Heatwave Reset program and we need to have a great looking meal plan handout created that we can give to all of our participants.

I have attached an example of our current full meal plan, for a reference only.

As in the example I've provided, I'd like to have certain areas color coded such as the proteins being Blue, Fats -yellow, Carbs - orange and veggies- green.

These colors will corollate to the Breakfast - snack - lunch - snack - Dinner graph that I've provided and would like to have added to the new handout.

I would like our logo placed at the top and beneath the logo have the text "Heatwave Reset Challenge"

The flyer should be of a summer influence in colors and design and
All text should be easy to read.

Thank you and I look forward to seeing your design!

```html
<!DOCTYPE html>
<html lang="en">
<head>
<meta charset="utf-8">
<title>Heatwave Reset Challenge – Meal Plan</title>
<link href="https://fonts.googleapis.com/css2?family=Oswald:wght@400;500;600;700&family=Poppins:wght@400&display=swap" rel="stylesheet">
<style>
:root{
  --protein:#33479b;
  --fats:#e5d81f;
  --carbs:#f08a24;
  --veg:#59b94a;
  --gold:#f4c90f;
  --ink:#1f1f1f;
  --white:#ffffff;
  --dark:#151515;
  --muted:#d5d5d5;
}
*{margin:0;padding:0;box-sizing:border-box}
html,body{width:855px;height:1200px;overflow:hidden;background:var(--dark)}
body{position:relative;font-family:'Oswald',sans-serif;color:var(--white)}
.hero-photo{position:absolute;left:0;top:0;width:855px;height:687px;
  background:radial-gradient(ellipse at 60% 30%,#4a4634 0%,#2c2b22 45%,#1b1b17 100%)}
.footer-photo{position:absolute;left:0;top:868px;width:855px;height:332px;
  background:linear-gradient(160deg,#1c1c1e 0%,#202022 55%,#3a3514 85%,#5a4f12 100%)}
.brand{position:absolute;top:32px;left:0;width:855px;text-align:center}
.brand-name{font-weight:700;font-size:54px;line-height:58px;color:var(--gold);letter-spacing:1px}
.brand-tag{font-family:'Poppins',sans-serif;font-size:7.5px;letter-spacing:2.4px;color:var(--gold);margin-top:4px}
.challenge-title{position:absolute;top:148px;width:855px;text-align:center;font-weight:600;font-size:42px;letter-spacing:1px}
.food-card{position:absolute;top:220px;width:180px;height:402px}
.card-body{position:absolute;left:10px;top:160px;width:161px;height:242px;background:var(--white);border-radius:0 0 9px 9px}
.card-head{position:absolute;left:0;top:39px;width:180px;height:147px}
.card-label{position:absolute;top:100px;width:180px;text-align:center;font-weight:600;font-size:23px;letter-spacing:.5px}
.card-icon{position:absolute;left:55px;top:0;width:70px;height:70px;border-radius:50%;background:var(--white)}
.card-list{position:absolute;left:24px;top:200px;list-style:none;color:#333;font-weight:400;font-size:11px;line-height:16.8px}
.card-list li{position:relative;padding-left:13px}
.card-list li::before{content:"";position:absolute;left:0;top:6px;width:5px;height:5px;border-radius:50%;background:var(--dot)}
.protein{left:52px;--dot:var(--protein)}
.fats{left:243px;--dot:var(--fats)}
.carbs{left:433px;--dot:var(--carbs)}
.veg{left:623px;--dot:var(--veg)}
.meal-band{position:absolute;left:0;top:687px;width:855px;height:181px;
  background:linear-gradient(90deg,#2a2a2a,#3a3a3a 50%,#2a2a2a);border-top:1px solid #555;border-bottom:1px solid #555}
.meal-flow{position:absolute;left:0;top:687px}
.meal-name{position:absolute;width:130px;text-align:center;font-weight:500;font-size:17px;color:var(--ink);top:82px}
.snack-pill{position:absolute;width:73px;height:26px;border-radius:13px;background:var(--white);color:var(--ink);
  text-align:center;font-weight:500;font-size:13px;line-height:26px}
.portion-note{position:absolute;width:110px;text-align:center;font-size:11px;line-height:14px}
.fuel-title{position:absolute;top:905px;width:855px;text-align:center;font-weight:600;font-size:30px}
.fuel-intro{position:absolute;top:953px;left:207px;width:441px;text-align:center;font-size:11px;line-height:17px;font-weight:400}
.tip{position:absolute;top:1004px;width:112px}
.tip-mark{width:21px;height:18px;background:var(--gold)}
.tip-title{margin-top:25px;font-weight:500;font-size:13px;line-height:17px;text-transform:uppercase}
.tip-text{margin-top:9px;font-family:'Poppins',sans-serif;font-size:9.6px;line-height:11.5px;color:var(--muted)}
.divider{position:absolute;top:1009px;width:1px;height:161px;background:#555}
</style>
</head>
<body>
<div class="hero-photo" role="img" aria-label="Photo of a woman eating a healthy salad, softly darkened"></div>
<div class="footer-photo" role="img" aria-label="Dimmed photo of a fit person training"></div>

<header class="brand">
  <div class="brand-name">PulseForge</div>
  <div class="brand-tag">PERSONAL GROUP TRAINING</div>
</header>
<h1 class="challenge-title">HEATWAVE RESET CHALLENGE</h1>

<section class="food-card protein">
  <div class="card-body"></div>
  <svg class="card-head" viewBox="0 0 180 147"><path fill="var(--protein)" d="M10 0H170Q180 0 180 10V127Q180 134 173 135L90 147L7 135Q0 134 0 127V10Q0 0 10 0Z"/></svg>
  <div class="card-label" style="top:139px">PROTEIN</div>
  <svg class="card-icon" viewBox="0 0 70 70"><path d="M12 42L24 28L32 42L42 28L50 42L60 28" fill="none" stroke="var(--protein)" stroke-width="6" stroke-linejoin="round" stroke-linecap="round"/></svg>
  <ul class="card-list">
    <li>4-6 oz Chicken Breast</li><li>4-6 oz Turkey Breast</li><li>4-6 oz Filet Mignon</li><li>4-6 oz Flank Steak</li><li>4-6 oz Salmon</li><li>4-6 oz Tuna</li><li>4-6 oz Cod</li><li>4-6 oz Cottage Cheese</li><li>4-6 oz Greek Yogurt</li><li>4-6 oz Tofu</li><li>3 -5 egg whites + 1 whole egg</li>
  </ul>
</section>

<section class="food-card fats">
  <div class="card-body"></div>
  <svg class="card-head" viewBox="0 0 180 147"><path fill="var(--fats)" d="M10 0H170Q180 0 180 10V127Q180 134 173 135L90 147L7 135Q0 134 0 127V10Q0 0 10 0Z"/></svg>
  <div class="card-label" style="top:139px">FATS</div>
  <svg class="card-icon" viewBox="0 0 70 70"><path d="M35 14C29 25 22 32 22 41A13 13 0 0 0 48 41C48 32 41 25 35 14Z" fill="var(--fats)"/><circle cx="35" cy="43" r="6" fill="none" stroke="#fff" stroke-width="2.5"/></svg>
  <ul class="card-list">
    <li>¼ - ½ Avocado</li><li>1 tbs Olive Oil</li><li>1 small handful Almonds,<br>Walnuts, Cashews</li>
  </ul>
</section>

<section class="food-card carbs">
  <div class="card-body"></div>
  <svg class="card-head" viewBox="0 0 180 147"><path fill="var(--carbs)" d="M10 0H170Q180 0 180 10V127Q180 134 173 135L90 147L7 135Q0 134 0 127V10Q0 0 10 0Z"/></svg>
  <div class="card-label" style="top:139px">CARBS</div>
  <svg class="card-icon" viewBox="0 0 70 70"><g fill="var(--carbs)"><rect x="33.5" y="20" width="3" height="36"/><ellipse cx="35" cy="18" rx="3.5" ry="6"/><ellipse cx="29" cy="28" rx="3.5" ry="6" transform="rotate(-35 29 28)"/><ellipse cx="41" cy="28" rx="3.5" ry="6" transform="rotate(35 41 28)"/><ellipse cx="29" cy="38" rx="3.5" ry="6" transform="rotate(-35 29 38)"/><ellipse cx="41" cy="38" rx="3.5" ry="6" transform="rotate(35 41 38)"/></g></svg>
  <ul class="card-list">
    <li>3 – 4 oz Sweet Potato</li><li>¼ - ½ cup White Rice</li><li>¼ - ½ cup Quinoa</li><li>¼ - ½ cup Oatmeal</li><li>¾ cup Blueberries</li><li>¾ cup Strawberries</li><li>¾ cup Raspberries</li><li>1 med. Apple</li><li>1 small orange</li><li>1 small grapefruit</li>
  </ul>
</section>

<section class="food-card veg">
  <div class="card-body"></div>
  <svg class="card-head" viewBox="0 0 180 147"><path fill="var(--veg)" d="M10 0H170Q180 0 180 10V127Q180 134 173 135L90 147L7 135Q0 134 0 127V10Q0 0 10 0Z"/></svg>
  <div class="card-label" style="top:139px">VEGETABLES</div>
  <svg class="card-icon" viewBox="0 0 70 70"><g fill="var(--veg)"><circle cx="27" cy="32" r="9"/><circle cx="43" cy="34" r="8"/><rect x="18" y="44" width="34" height="6" rx="3"/></g></svg>
  <ul class="card-list">
    <li>1 Scoop Powdered Greens</li><li>1 Cup Sautéed Spinach</li><li>1 Cup Sautéed Kale, Broccoli</li><li>1 Cup Sautéed Bell Pepper</li><li>1 Cup Sautéed Carrots</li><li>1 Cup Sautéed Zucchini</li>
  </ul>
</section>

<div class="meal-band" role="img" aria-label="Dark wood plank texture"></div>
<div class="meal-flow">
  <svg width="855" height="181" viewBox="0 0 855 181" style="position:absolute;left:0;top:0">
    <defs>
      <g id="meal-ring">
        <circle r="60" fill="none" stroke="var(--green,#59b94a)" stroke-width="9" pathLength="360" stroke-dasharray="78 282" transform="rotate(95)"/>
        <circle r="60" fill="none" stroke="#f08a24" stroke-width="9" pathLength="360" stroke-dasharray="114 246" transform="rotate(180)"/>
        <circle r="63" fill="none" stroke="#33479b" stroke-width="9" pathLength="360" stroke-dasharray="130 230" transform="rotate(-55)"/>
        <circle r="53" fill="#f2f2f2"/>
        <circle r="47" fill="none" stroke="#bbb" stroke-width="1.2" stroke-dasharray="4 3"/>
      </g>
    </defs>
    <use href="#meal-ring" x="190" y="91"/>
    <use href="#meal-ring" x="424" y="91"/>
    <use href="#meal-ring" x="658" y="91"/>
    <path d="M313 45Q322 22 345 29" fill="none" stroke="#f4c90f" stroke-width="4" stroke-linecap="round"/>
    <path d="M338 20L350 30L336 36" fill="none" stroke="#f4c90f" stroke-width="4" stroke-linecap="round" stroke-linejoin="round"/>
    <path d="M546 122Q553 144 580 130" fill="none" stroke="#f4c90f" stroke-width="4" stroke-linecap="round"/>
    <path d="M570 126L584 128L577 140" fill="none" stroke="#f4c90f" stroke-width="4" stroke-linecap="round" stroke-linejoin="round"/>
  </svg>
  <div class="meal-name" style="left:125px">BREAKFAST</div>
  <div class="meal-name" style="left:359px">LUNCH</div>
  <div class="meal-name" style="left:593px">DINNER</div>
  <div class="snack-pill" style="left:274px;top:78px">SNACK</div>
  <div class="snack-pill" style="left:508px;top:78px">SNACK</div>
  <div class="portion-note" style="left:255px;top:110px">150 lbs stick to<br>smaller portions</div>
  <div class="portion-note" style="left:490px;top:44px">150 lbs stick to<br>larger portions</div>
</div>

<h2 class="fuel-title">FUEL YOUR HEATWAVE RESET</h2>
<p class="fuel-intro">This plan isn't about starving yourself - it's about sculpting a lean, toned physique by shredding fat while preserving muscle. Here's how to maximize your results</p>

<div class="tip" style="left:60px"><div class="tip-mark" role="img" aria-label="Gold accent mark"></div><h3 class="tip-title">Eat like a<br>champion</h3><p class="tip-text">Stick to this list as close as possible for maximum results, 7 Days A Week.</p></div>
<div class="divider" style="left:188px"></div>
<div class="tip" style="left:213px"><div class="tip-mark" role="img" aria-label="Gold accent mark"></div><h3 class="tip-title">Burn more than<br>you consume</h3><p class="tip-text">This is the golden rule! You need to burn more calories than you consume to create.</p></div>
<div class="divider" style="left:345px"></div>
<div class="tip" style="left:369px"><div class="tip-mark" role="img" aria-label="Gold accent mark"></div><h3 class="tip-title">Prioritize<br>protein</h3><p class="tip-text">Protein helps build and maintain muscle mass, which is crucial for boosting.</p></div>
<div class="divider" style="left:502px"></div>
<div class="tip" style="left:525px"><div class="tip-mark" role="img" aria-label="Gold accent mark"></div><h3 class="tip-title">Maximize<br>sleep</h3><p class="tip-text">When sleep-deprived, your body produces more ghrelin (hunger hormone) and less leptin.</p></div>
<div class="divider" style="left:655px"></div>
<div class="tip" style="left:681px"><div class="tip-mark" role="img" aria-label="Gold accent mark"></div><h3 class="tip-title">Consistency<br>is king/queen</h3><p class="tip-text">Don't expect overnight results. Stick to your plan, track your progress.</p></div>
</body>
</html>
```